This book will apply the 12 Steps to gaming addiction, also known as video game addiction. The primary purpose of the book is to provide an effective solution for this new type of addiction. The solution is based on the rich and successful concepts of traditional twelve-step programs like RL.

The title on the cover will be "Nine Doors Past the Glowing Screen" and "by Martin Quorby". A subtitle can be used if it works in your design of "A Practical Path Beyond Compulsive Console Play". Cover will be for a 6" x 9" book approximately 110 pages in length.

Some back cover text including some review quotes and an author bio are in the attached Word doc. There is also an author photo attached for for the back cover.

Requirements
Must have
• For the cover design it could be stylized, or an image, a partial image, or whatever. I am open to suggestions. Think about what would be noticed by a person searching for help with moderating their video game use, or by the parents or loved ones of problem gamers. Something contemporary and eye catching.

```html
<!DOCTYPE html>
<html lang="en">
<head>
<meta charset="utf-8">
<title>Nine Doors Past the Glowing Screen — Front Cover</title>
<link rel="stylesheet" href="https://fonts.googleapis.com/css2?family=Poppins:wght@400;500&family=Cormorant+Garamond:wght@500;700&display=swap">
<style>
  :root {
    --backdrop: #d4d6be;
    --cover-black: #151413;
    --ink-white: #ffffff;
    --accent-yellow: #f2b620;
    --photo-light: #b3a594;
    --photo-warm: #857869;
    --photo-mid: #4f4740;
    --photo-deep: #2a2623;
    --photo-dark: #1a1817;
  }
  * { margin: 0; padding: 0; box-sizing: border-box; }
  html, body {
    width: 1200px;
    height: 864px;
    overflow: hidden;
    background: var(--backdrop);
  }
  .canvas {
    position: relative;
    width: 1200px;
    height: 864px;
  }
  .front-cover {
    position: absolute;
    left: 333px;
    top: 32px;
    width: 533px;
    height: 800px;
    background: var(--cover-black);
    overflow: hidden;
    font-family: "Poppins", sans-serif;
  }
  .cover-photo {
    position: absolute;
    left: 0;
    top: 250px;
    width: 533px;
    height: 550px;
    background:
      radial-gradient(ellipse 22% 16% at 58% 28%, var(--photo-light) 0%, transparent 100%),
      radial-gradient(ellipse 24% 18% at 56% 62%, var(--photo-light) 0%, transparent 100%),
      radial-gradient(ellipse 40% 42% at 58% 46%, var(--photo-warm) 0%, var(--photo-mid) 55%, transparent 100%),
      radial-gradient(ellipse 22% 20% at 30% 40%, #0c0c0c 0%, transparent 100%),
      radial-gradient(ellipse 30% 10% at 86% 14%, var(--photo-mid) 0%, transparent 100%),
      radial-gradient(ellipse 70% 60% at 55% 48%, var(--photo-deep) 0%, var(--photo-dark) 70%, var(--cover-black) 100%);
  }
  .title-block { position: absolute; inset: 0; z-index: 2; }
  .title-kicker {
    position: absolute;
    left: 58px;
    top: 104px;
    font-family: "Cormorant Garamond", serif;
    font-weight: 700;
    font-size: 11px;
    letter-spacing: 0.04em;
    color: var(--ink-white);
  }
  .title-numeral {
    position: absolute;
    left: 54px;
    top: 112px;
    font-size: 92px;
    font-weight: 400;
    line-height: 1;
    letter-spacing: -0.02em;
    color: var(--ink-white);
  }
  .title-lead {
    position: absolute;
    left: 292px;
    top: 104px;
    font-size: 50px;
    font-weight: 500;
    line-height: 1;
    color: var(--accent-yellow);
  }
  .title-link {
    position: absolute;
    left: 294px;
    top: 160px;
    font-size: 20px;
    font-weight: 500;
    letter-spacing: 0.04em;
    line-height: 1;
    color: var(--ink-white);
  }
  .title-band {
    position: absolute;
    font-size: 42px;
    font-weight: 400;
    line-height: 1;
    padding: 4px 10px 2px;
  }
  .title-band--yellow {
    left: 214px;
    top: 196px;
    background: var(--accent-yellow);
    color: var(--ink-white);
  }
  .title-band--white {
    left: 54px;
    top: 244px;
    background: var(--ink-white);
    color: var(--accent-yellow);
  }
  .author-name {
    position: absolute;
    z-index: 2;
    left: 190px;
    right: 30px;
    top: 672px;
    text-align: center;
    font-family: "Cormorant Garamond", serif;
    font-weight: 500;
    font-size: 19px;
    letter-spacing: 0.42em;
    color: var(--ink-white);
  }
</style>
</head>
<body>
<main class="canvas">
  <section class="front-cover" aria-label="Front cover of Nine Doors Past the Glowing Screen">
    <div class="cover-photo" role="img" aria-label="Sepia photograph of two fists bound in heavy iron chain while gripping a game controller, against a dark background"></div>
    <h1 class="title-block">
      <span class="title-kicker">THE</span>
      <span class="title-numeral">NINE</span>
      <span class="title-lead">DOORS</span>
      <span class="title-link">PAST THE</span>
      <span class="title-band title-band--yellow">GLOWING</span>
      <span class="title-band title-band--white">SCREEN</span>
    </h1>
    <p class="author-name">MARTIN QUORBY</p>
  </section>
</main>
</body>
</html>
```